Quillon Energy Business Cards

I would like to design some options for about 10 sets of double sided business cards for our team with a raised logo with a Silver glossy finished logo. We are a privately funded upstream Oil & Gas producer drilling vertical wells in Central Oklahoma with a long term production (ROI driven) strategy that we implement through an annual drilling program. We are focused on a shallow / vertical / long life / low decline strategy. We are based in downtown Tulsa Oklahoma. I have attached a sample business card and a picture of our hallway logo which we would like to replicate on the business cards.

Target Market(s)

BRQ Accredited Investors and other Oil & Gas Operators

Industry/Entity Type

Upstream Oil & Gas

Contact Information for Business Card

You can see the sample photo attached, but email / website / address / direct phone / Cell Phone / Name / Title / Fax

Font styles to use
Other font styles liked:
• Felix Titling

Colors
0054AA
0677BA
7BADD7
CADEEF
E8F1F8

Requirements
Must have
• Glossy raised logo
Nice to have
• Possibly a new logo.
Should not have
• No Greens /

```html
<!DOCTYPE html>
<html lang="en">
<head>
<meta charset="utf-8">
<title>Quillon Energy Business Cards</title>
<link href="https://fonts.googleapis.com/css2?family=Cinzel:wght@400;600&display=swap" rel="stylesheet">
<style>
  :root {
    --bg: #3b3b3c;
    --card-dark: #2c2728;
    --card-dark-hi: #37302f;
    --gold: #a7832f;
    --gold-deep: #8c6a22;
    --white: #f4f2ee;
    --ink: #1e1a1a;
  }
  * { margin: 0; padding: 0; box-sizing: border-box; }
  html, body { width: 1200px; height: 1200px; overflow: hidden; }
  body {
    background: var(--bg);
    font-family: "Cinzel", serif;
    display: flex;
    flex-direction: column;
    align-items: center;
    justify-content: center;
    gap: 44px;
  }
  .card {
    position: relative;
    width: 900px;
    height: 514px;
    background: radial-gradient(circle at 60% 35%, var(--card-dark-hi), var(--card-dark) 70%);
    overflow: hidden;
    box-shadow: 0 10px 30px rgba(0,0,0,.35);
  }
  /* back */
  .card-back .brand {
    position: absolute;
    left: 0; right: 0; top: 205px;
    text-align: center;
    color: var(--white);
    font-size: 46px;
    font-weight: 600;
    letter-spacing: 1px;
  }
  .card-back .website {
    position: absolute;
    left: 0; right: 0; top: 290px;
    text-align: center;
    color: var(--white);
    font-size: 20px;
    letter-spacing: .5px;
  }
  .website .accent { color: var(--gold); }
  /* front */
  .card-front .shapes { position: absolute; inset: 0; }
  .holder { position: absolute; left: 270px; top: 42px; }
  .holder-name { color: var(--gold); font-size: 34px; letter-spacing: 1px; }
  .holder-title, .holder-dept { color: var(--white); font-size: 17px; margin-top: 4px; }
  .holder-title { margin-left: -22px; margin-top: 8px; }
  .holder-dept { margin-left: -40px; }
  .contact {
    position: absolute;
    left: 120px; top: 230px;
    color: var(--white);
    font-size: 17px;
    line-height: 1.55;
  }
  .contact .address { margin-bottom: 10px; }
  .contact .line { display: flex; align-items: center; gap: 10px; }
  .contact svg { width: 16px; height: 16px; fill: var(--ink); flex: none; }
  .card-front .brand {
    position: absolute;
    left: 580px; top: 235px;
    color: var(--white);
    font-size: 24px;
    font-weight: 600;
  }
</style>
</head>
<body>

<section class="card card-back" aria-label="Card back">
  <div class="brand">Quillon Energy, LLC</div>
  <div class="website"><span class="accent">www.</span>quillonenergyllc<span class="accent">.com</span></div>
</section>

<section class="card card-front" aria-label="Card front">
  <svg class="shapes" viewBox="0 0 900 514" preserveAspectRatio="none" aria-hidden="true">
    <defs>
      <linearGradient id="goldFill" x1="0" y1="0" x2="0.4" y2="1">
        <stop offset="0" stop-color="#ad8a36"/>
        <stop offset="1" stop-color="#8c6a22"/>
      </linearGradient>
    </defs>
    <path class="gold-field" d="M0,200 C250,170 520,330 595,514 L0,514 Z" fill="url(#goldFill)"/>
    <path class="gold-arc" d="M480,235 C590,300 670,390 695,514 L620,514 C590,410 550,310 480,235 Z" fill="url(#goldFill)"/>
    <path class="gold-corner" d="M710,514 L708,400 C770,440 850,390 900,320 L900,514 Z" fill="url(#goldFill)"/>
  </svg>

  <div class="holder">
    <div class="holder-name">Darian P. Whitcombe, CPL</div>
    <div class="holder-title">Executive Vice President</div>
    <div class="holder-dept">Land, Legal &amp; Business Development</div>
  </div>

  <div class="contact">
    <div class="address">42 West 9th St<br>Suite 800 Tulsa, OK 74103</div>
    <div class="line">
      <svg viewBox="0 0 24 24"><path d="M6.6 10.8a15 15 0 0 0 6.6 6.6l2.2-2.2c.3-.3.7-.4 1-.2 1.1.4 2.3.6 3.6.6.6 0 1 .4 1 1V20c0 .6-.4 1-1 1A17 17 0 0 1 3 4c0-.6.4-1 1-1h3.5c.6 0 1 .4 1 1 0 1.3.2 2.5.6 3.6.1.3 0 .7-.2 1z"/></svg>
      <span>555-210-4831</span>
    </div>
    <div class="line">
      <svg viewBox="0 0 24 24"><path d="M7 1h10a2 2 0 0 1 2 2v18a2 2 0 0 1-2 2H7a2 2 0 0 1-2-2V3a2 2 0 0 1 2-2zm0 3v14h10V4zm5 15.5a1 1 0 1 0 0 2 1 1 0 0 0 0-2z"/></svg>
      <span>555-374-9062</span>
    </div>
    <div class="line">
      <svg viewBox="0 0 24 24"><path d="M6 2h12v5H6zM4 8h16a2 2 0 0 1 2 2v7h-4v5H6v-5H2v-7a2 2 0 0 1 2-2zm4 8v4h8v-4z"/></svg>
      <span>555-618-2047</span>
    </div>
    <div class="line">
      <svg viewBox="0 0 24 24"><path d="M2 5h20v14H2zm2 2v.5l8 5 8-5V7z"/></svg>
      <span>DPW@qetulsa.com</span>
    </div>
  </div>

  <div class="brand">Quillon Energy, LLC</div>
</section>

</body>
</html>
```